Call to action - Postcard Design

Design a post card keeping in mind the following;

1. double sided
2. 4" x6" (10.16cm x 15.24cm)
3. call to action message "Fast Free Quote" using a similar feel to our trade show booth design and brochure.
5. need to include the four vertical market logos "cameras, access, alarm, intercom"
6. an image and brief description on the back of the postcard with the call to action;
a. Camera Systems "easy to use software, remote monitoring from any device, motion activated"
b. Access Control "web browser credential management and allow/deny access from anywhere"
7. review our slides on the front page of our website http://www.keplowmart.com

Target Market(s)

B2B - business owners, managers, purchasers

Industry/Entity Type

Call

Requirements
Must have
• - call to action to get clients to contact us for a free quote
• - use a similar design to our trade show booth
• - clean look (uncluttered)

```html
<!DOCTYPE html>
<html lang="en">
<head>
<meta charset="utf-8">
<title>Keplow Mart – Fast Free Quote Postcard</title>
<link href="https://fonts.googleapis.com/css2?family=Lato:wght@300;400;700&family=Oswald:wght@400;500&family=Raleway:wght@300;400;700;800&display=swap" rel="stylesheet">
<style>
  :root {
    --navy: #2f3c5c;
    --navy-deep: #1f3a5f;
    --orange: #e8533a;
    --white: #ffffff;
    --card: #fdfdfd;
    --border: #c9c9c9;
    --text: #666a70;
    --label: #1f3a5f;
  }
  * { margin: 0; padding: 0; box-sizing: border-box; }
  html, body { width: 1200px; height: 1200px; overflow: hidden; background: var(--white); }
  body { position: relative; font-family: "Lato", sans-serif; }

  .front {
    position: absolute; left: 156px; top: 0; width: 888px; height: 592px;
    background: var(--navy); color: var(--white);
  }
  .brand {
    position: absolute; display: flex; align-items: center; gap: 8px;
    font-family: "Lato", sans-serif; font-weight: 700; letter-spacing: 1px;
  }
  .brand__square { width: 12px; height: 12px; background: currentColor; }
  .front .brand { left: 268px; top: 68px; font-size: 16px; color: var(--white); }
  .team-figure {
    position: absolute; left: 266px; top: 122px; width: 356px; height: 89px;
    background: linear-gradient(90deg, rgba(255,255,255,.85) 0%, rgba(255,255,255,.85) 76%, var(--orange) 80%, var(--orange) 86%, rgba(255,255,255,.85) 90%);
    opacity: .9;
  }
  .headline {
    position: absolute; left: 0; right: 0; top: 298px; text-align: center;
    font-family: "Raleway", sans-serif; font-weight: 300; font-size: 84px; letter-spacing: 2px; white-space: nowrap;
  }
  .headline__accent { color: var(--orange); font-weight: 800; font-style: italic; letter-spacing: 3px; }

  .markets { position: absolute; display: flex; }
  .market { display: flex; flex-direction: column; align-items: center; }
  .market__icon { border-radius: 50%; display: flex; align-items: center; justify-content: center; }
  .market__label { font-family: "Oswald", sans-serif; white-space: nowrap; }

  .front .markets { left: 309px; top: 473px; gap: 12px; }
  .front .market { width: 58px; }
  .front .market__icon { width: 58px; height: 58px; border: 2px solid var(--white); background: var(--navy); }
  .front .market__label { margin-top: 6px; font-size: 15px; color: var(--white); }
  .front .market svg { stroke: var(--white); }

  .back {
    position: absolute; left: 156px; top: 608px; width: 888px; height: 590px;
    background: var(--card); border: 1.5px solid var(--border);
  }
  .feature { position: absolute; left: 28px; }
  .feature__title { font-family: "Raleway", sans-serif; font-size: 28px; line-height: 26px; font-weight: 400; color: var(--orange); }
  .feature__sub { font-family: "Raleway", sans-serif; font-size: 26px; line-height: 28px; color: var(--navy-deep); letter-spacing: 1px; }
  .feature__sub b { font-weight: 800; }
  .feature__text { margin-top: 6px; font-size: 16px; line-height: 20px; color: var(--text); }
  .feature--cameras { top: 56px; }
  .feature--access { top: 202px; }

  .product-scene {
    position: absolute; left: 400px; top: 32px; width: 456px; height: 228px;
    background: linear-gradient(135deg, #e9ecef 0%, #cfd5db 45%, #6f7a70 60%, #e6e8ea 100%);
    border-radius: 4px;
  }

  .back .markets { left: 639px; top: 257px; gap: 10px; }
  .back .market { width: 46px; }
  .back .market__icon { width: 46px; height: 46px; border: 2px solid var(--label); background: var(--white); }
  .back .market__icon svg { width: 26px; height: 26px; stroke: var(--label); }
  .back .market__label { margin-top: 4px; font-size: 12px; font-weight: 500; color: var(--label); }

  .pitch {
    position: absolute; left: 29px; top: 362px; width: 832px;
    font-size: 16px; line-height: 27px; color: var(--text); letter-spacing: -0.2px;
  }
  .back .brand {
    left: 0; right: 0; top: 470px; justify-content: center; gap: 12px;
    font-size: 30px; color: var(--navy-deep); letter-spacing: 1px;
  }
  .back .brand__square { width: 22px; height: 22px; }
  .contact {
    position: absolute; left: 29px; right: 26px; top: 550px; display: flex; justify-content: space-between;
    font-size: 11px; letter-spacing: 4.8px; color: var(--text); white-space: nowrap;
  }
</style>
</head>
<body>

<section class="front">
  <div class="brand"><span class="brand__square"></span>KEPLOW MART</div>
  <div class="team-figure" role="img" aria-label="Row of nine standing people pictograms, one highlighted in orange"></div>
  <h1 class="headline"><span class="headline__accent">FAST</span> FREE QUOTE</h1>
  <div class="markets">
    <div class="market">
      <div class="market__icon"><svg width="32" height="32" viewBox="0 0 32 32" fill="none" stroke-width="2"><rect x="6" y="12" width="18" height="9" rx="1"/><path d="M24 14l5-2v9l-5-2"/><path d="M12 21v5M8 26h8"/></svg></div>
      <span class="market__label">Cameras</span>
    </div>
    <div class="market">
      <div class="market__icon"><svg width="58" height="58" viewBox="0 0 58 58" fill="none" stroke-width="2"><circle cx="34" cy="22" r="6"/><path d="M30 26L16 40M19 37l3 3M22 34l3 3"/><path d="M10 10l38 38"/></svg></div>
      <span class="market__label">Access</span>
    </div>
    <div class="market">
      <div class="market__icon"><svg width="32" height="32" viewBox="0 0 32 32" fill="none" stroke-width="2"><rect x="8" y="5" width="16" height="22" rx="2"/><rect x="11" y="8" width="10" height="5"/><path d="M12 17h2M18 17h2M12 21h2M18 21h2"/></svg></div>
      <span class="market__label">Alarm</span>
    </div>
    <div class="market">
      <div class="market__icon"><svg width="32" height="32" viewBox="0 0 32 32" fill="none" stroke-width="2"><path d="M9 8v10M13 7v11M17 7v11M21 7v11M25 8v10"/><path d="M6 21c5 5 15 5 22 0"/></svg></div>
      <span class="market__label">Intercom</span>
    </div>
  </div>
</section>

<section class="back">
  <div class="feature feature--cameras">
    <h2 class="feature__title">CAMERA SYSTEMS</h2>
    <p class="feature__sub"><b>EASY</b> TO USE</p>
    <p class="feature__text">Remote monitoring from any<br>device, motion activated</p>
  </div>
  <div class="feature feature--access">
    <h2 class="feature__title">ACCESS CONTROL</h2>
    <p class="feature__sub">YOU CAN USE <b>ANYWHERE</b></p>
    <p class="feature__text">Web browser credential management and<br>allow/deny access from anywhere</p>
  </div>

  <div class="product-scene" role="img" aria-label="Monitor showing camera video feeds, a dome security camera and a door with a green unlock badge"></div>

  <div class="markets">
    <div class="market">
      <div class="market__icon"><svg viewBox="0 0 32 32" fill="none" stroke-width="2.4"><rect x="6" y="12" width="18" height="9" rx="1"/><path d="M24 14l5-2v9l-5-2"/><path d="M12 21v5M8 26h8"/></svg></div>
      <span class="market__label">Cameras</span>
    </div>
    <div class="market">
      <div class="market__icon"><svg viewBox="0 0 32 32" fill="none" stroke-width="2.4"><circle cx="19" cy="12" r="4"/><path d="M16 15L8 23M10 21l2 2M12 19l2 2"/><path d="M4 4l24 24"/></svg></div>
      <span class="market__label">Access</span>
    </div>
    <div class="market">
      <div class="market__icon"><svg viewBox="0 0 32 32" fill="none" stroke-width="2.4"><rect x="8" y="5" width="16" height="22" rx="2"/><rect x="11" y="8" width="10" height="5"/><path d="M12 17h2M18 17h2M12 21h2M18 21h2"/></svg></div>
      <span class="market__label">Alarm</span>
    </div>
    <div class="market">
      <div class="market__icon"><svg viewBox="0 0 32 32" fill="none" stroke-width="2.4"><path d="M9 8v10M13 7v11M17 7v11M21 7v11M25 8v10"/><path d="M6 21c5 5 15 5 22 0"/></svg></div>
      <span class="market__label">Intercom</span>
    </div>
  </div>

  <p class="pitch">Our projects include everything from small business to multi site enterprise corporations — we are just happy to get the opportunity from you — whatever that might be. We invite you to request a demonstration, call our references or just get crazy and give us a chance to prove to you that we are the right firm to handle all of your security.</p>

  <div class="brand"><span class="brand__square"></span>KEPLOW MART</div>

  <div class="contact">
    <span>TOLL FREE: 800.555.0142</span>
    <span>|</span>
    <span>SALES@KEPLOWMART.COM</span>
    <span>|</span>
    <span>WWW.KEPLOWMART.COM</span>
  </div>
</section>

</body>
</html>
```